Animated custom graphic for hero section of web site home page

I would like a custom graphic that will be used on my new web site home page (see attached image). The graphic must represent revenue growth against projected sales performance. A stylish graph-like image that animates the budget vs. sales results over 12 months could be good. Do some Torvix research for some inspiration.

See the attached example. I want something a bit more stylish. The 2 lines you see on the chart should be animated. The Budget line comes first, then the Actual.

Target Market(s)

CEOs / Founders of B2B SaaS / Tech companies

Industry/Entity Type

SaaS, IT, Tech, Management consulting.

Requirements
Must have
• The custom graphic must represent revenue growth, success etc. Possibly a UI mockup of a CRM dashboard showing quarterly achievement of hitting sales target.The custom graphic must be original, unique and versatile to be used as a custom graphic on ANY web site design with little or no modification. The custom graphic should either use 1 or 2 colors only (black and white)
Nice to have
• ANIMATED - Maybe show a stylish graph with two lines of sales achievement (actual vs. budget) - lines (not bar graph). First the budget line comes up and then the animation shows the actual achieved results) which is better.
Should not have
• No clipart / cartoon style graphics

```html
<!DOCTYPE html>
<html lang="en">
<head>
<meta charset="UTF-8">
<title>Northpeak – Fractional GTM Leadership</title>
<link href="https://fonts.googleapis.com/css2?family=Poppins:wght@400;500;600;700&display=swap" rel="stylesheet">
<style>
  :root {
    --teal: #45b5a6;
    --teal-grid: rgba(255,255,255,0.16);
    --teal-bar: rgba(255,255,255,0.09);
    --white: #ffffff;
    --ink: #1f2a2e;
    --budget: rgba(255,255,255,0.75);
    --actual: rgba(31,42,46,0.55);
  }
  * { margin: 0; padding: 0; box-sizing: border-box; }
  html, body { width: 1200px; height: 576px; overflow: hidden; }
  body {
    font-family: "Poppins", sans-serif;
    color: var(--white);
    background: var(--teal);
  }
  .hero {
    position: relative;
    width: 1200px;
    height: 576px;
    overflow: hidden;
    background-color: var(--teal);
    background-image:
      linear-gradient(var(--teal-grid) 1px, transparent 1px),
      linear-gradient(90deg, var(--teal-grid) 1px, transparent 1px);
    background-size: 40px 40px;
    background-position: 2px 6px;
  }
  .revenue-chart { position: absolute; left: 0; top: 0; width: 1200px; height: 576px; }
  .chart-line {
    fill: none;
    stroke-linecap: round;
    stroke-linejoin: round;
    stroke-dasharray: 1;
    stroke-dashoffset: 1;
  }
  .line-budget {
    stroke: var(--budget);
    stroke-width: 2.5;
    animation: draw-line 2.2s ease-out 0.3s forwards;
  }
  .line-actual {
    stroke: var(--actual);
    stroke-width: 3.5;
    animation: draw-line 2.6s ease-out 2.7s forwards;
  }
  .chart-point { opacity: 0; animation: show-point 0.4s ease-out forwards; }
  .point-budget { fill: var(--white); animation-delay: 2.5s; }
  .point-actual { fill: var(--ink); animation-delay: 5.3s; }
  @keyframes draw-line { to { stroke-dashoffset: 0; } }
  @keyframes show-point { to { opacity: 1; } }

  .brand {
    position: absolute; left: 83px; top: 22px;
    font-size: 19px; font-weight: 700; letter-spacing: 0.2px;
  }
  .nav { position: absolute; top: 26px; left: 672px; list-style: none; font-size: 12.5px; font-weight: 500; }
  .nav li { position: absolute; white-space: nowrap; }
  .nav li:nth-child(1) { left: 0; }
  .nav li:nth-child(2) { left: 75px; }
  .nav li:nth-child(3) { left: 147px; }
  .nav li:nth-child(4) { left: 230px; }
  .btn {
    position: absolute;
    background: var(--ink);
    color: var(--white);
    border-radius: 6px;
    display: flex; align-items: center; justify-content: center;
    font-size: 13px; font-weight: 400;
    box-shadow: 0 2px 6px rgba(0,0,0,0.12);
  }
  .btn-header { left: 990px; top: 15px; width: 127px; height: 41px; }
  .btn-cta { left: 83px; top: 343px; width: 337px; height: 49px; }
  .headline {
    position: absolute; left: 83px; top: 138px;
    font-size: 49px; font-weight: 700; line-height: 55px; letter-spacing: 0.2px;
  }
  .subhead {
    position: absolute; left: 83px; top: 267px; width: 680px;
    font-size: 16px; font-weight: 400; line-height: 28px;
  }
  .clients { position: absolute; top: 460px; left: 0; width: 100%; height: 30px; font-weight: 500; }
  .client { position: absolute; white-space: nowrap; display: flex; align-items: center; gap: 7px; height: 28px; }
  .client-mark { width: 10px; height: 10px; background: var(--white); }
  .client:nth-child(1) { left: 83px; font-size: 21px; }
  .client:nth-child(2) { left: 202px; font-size: 21px; }
  .client:nth-child(3) { left: 317px; font-size: 16px; font-weight: 600; }
  .client:nth-child(4) { left: 450px; font-size: 12px; font-weight: 600; }
  .client:nth-child(5) { left: 627px; font-size: 20px; font-weight: 700; }
  .client:nth-child(6) { left: 714px; font-size: 16px; font-weight: 700; }
</style>
</head>
<body>
<section class="hero">
  <svg class="revenue-chart" viewBox="0 0 1200 576" role="img" aria-label="Animated twelve-month revenue chart: budget line drawn first, then actual sales line rising above it">
    <g class="chart-bars">
      <rect x="83" y="540" width="45" height="36" fill="var(--teal-bar)"/>
      <rect x="158" y="522" width="50" height="54" fill="var(--teal-bar)"/>
      <rect x="306" y="410" width="50" height="166" fill="var(--teal-bar)"/>
      <rect x="383" y="385" width="50" height="191" fill="var(--teal-bar)"/>
      <rect x="460" y="332" width="50" height="244" fill="var(--teal-bar)"/>
      <rect x="614" y="292" width="50" height="284" fill="var(--teal-bar)"/>
      <rect x="690" y="270" width="50" height="306" fill="var(--teal-bar)"/>
      <rect x="786" y="165" width="330" height="411" fill="rgba(255,255,255,0.05)"/>
    </g>
    <path class="chart-line line-budget" pathLength="1"
      d="M83 548 L170 530 L256 508 L342 484 L428 458 L514 430 L600 400 L686 368 L772 334 L858 298 L944 260 L1030 222 L1117 182"/>
    <path class="chart-line line-actual" pathLength="1"
      d="M83 556 L170 536 L256 520 L342 478 L428 470 L514 418 L600 410 L686 352 L772 326 L858 268 L944 238 L1030 186 L1117 140"/>
    <circle class="chart-point point-budget" cx="1117" cy="182" r="5"/>
    <circle class="chart-point point-actual" cx="1117" cy="140" r="6"/>
  </svg>

  <div class="brand">Northpeak</div>

  <ul class="nav">
    <li>Demos</li>
    <li>Pages</li>
    <li>Support</li>
    <li>Contact</li>
  </ul>

  <div class="btn btn-header">Get Started Now</div>

  <h1 class="headline">Fractional GTM<br>Leadership For SaaS Firms</h1>

  <p class="subhead">Unlock your SaaS Hypergrowth Potential Propelling from Launch to $1M ARR | Scaling Predictably to $30M ARR</p>

  <div class="btn btn-cta">Take a 2-Min Assessment to Secure a Spot</div>

  <div class="clients">
    <span class="client">lumora</span>
    <span class="client">Vextra</span>
    <span class="client">Skyline</span>
    <span class="client">Rahim &amp; Sons Co.</span>
    <span class="client">Kivo</span>
    <span class="client">Tidewell <span class="client-mark"></span></span>
  </div>
</section>
</body>
</html>
```